Brand Voice Blueprint Book Cover Design

I'm about to publish the English version of my book on Brand Voice Blueprint. Name of the book is "Brand Voice Blueprint – How to untangle the online attention puzzle and leave your rivals behind". As a reference for colors and visual identity, I'm attaching the original book cover in Portuguese. I cannot reproduce the same cover due to my editor's copyright. I'm open to new fonts, font colors and illustrations that works well with the book title. I prefer a white or close to white solid or gradient background. I only need the front cover since the book will be published as an ebook format. The cover should show the title, subtitle, 3rd edition and my name "Tomas Veradello".

Target Market(s)

ebook publication on strategy / business

Industry/Entity Type

Business Management

Font styles to use
Sans Serif

Requirements
Must have
• The cover should show the title, subtitle, 3rd edition and my name "Tomas Veradello". White background. Should include a smart illustration that relates to the title. Illustration can be full of colors or more abstract. Use of shadows around the illustration is also ok. Keywords: social media, paradox, your company vs competitor, dialog, connection.
Nice to have
• Use the same visual identity from the first cover (attached).
Should not have
• Avoid the use of social media icons (from services like Chatterloom, Glimmerbox, etc.) or other kinds of icons such as phone, feed, wifi, etc.

```html
<!DOCTYPE html>
<html lang="en">
<head>
<meta charset="utf-8">
<title>Brand Voice Blueprint – Cover</title>
<link rel="stylesheet" href="https://fonts.googleapis.com/css2?family=Russo+One&display=swap">
<style>
  :root {
    --paper: #ffffff;
    --ink: #0b0b0b;
    --white: #ffffff;
    --red: #e8302a;
    --orange: #f7a21b;
    --blue: #3fa8e6;
    --yellow: #f3c12a;
    --rim: #f0a63a;
    --text-dark: #2a2a2a;
  }
  * { margin: 0; padding: 0; box-sizing: border-box; }
  html, body { width: 849px; height: 1200px; overflow: hidden; background: var(--paper); }
  .cover {
    position: relative;
    width: 849px;
    height: 1200px;
    overflow: hidden;
    background: var(--paper);
    font-family: "Russo One", sans-serif;
  }
  .network-backdrop {
    position: absolute;
    inset: 0;
    background:
      radial-gradient(ellipse 60% 50% at 62% 70%, #c9c9c9 0%, rgba(201,201,201,0) 72%),
      linear-gradient(160deg, #e6e6e6 0%, #f4f4f4 45%, #dcdcdc 100%);
  }
  .spine-line {
    position: absolute;
    left: 500px;
    top: 150px;
    width: 10px;
    height: 855px;
    background: var(--ink);
  }
  .author-plate {
    position: absolute;
    left: 226px;
    top: 172px;
    width: 380px;
    height: 76px;
    background: var(--ink);
    border: 3px solid var(--rim);
    display: flex;
    align-items: center;
    justify-content: center;
    color: var(--white);
    font-size: 30px;
    letter-spacing: 0.5px;
    white-space: nowrap;
  }
  .title-block {
    position: absolute;
    left: 113px;
    top: 505px;
    width: 651px;
    height: 372px;
    background: var(--ink);
  }
  .title {
    position: absolute;
    left: 128px;
    top: 522px;
    font-weight: 400;
    line-height: 1.05;
    font-size: 100px;
    letter-spacing: 1px;
    white-space: nowrap;
    -webkit-text-stroke: 5px var(--white);
    paint-order: stroke fill;
  }
  .title span { display: block; }
  .title .word-brand { color: var(--red); }
  .title .word-voice { color: var(--orange); -webkit-text-stroke-color: #fff3c4; }
  .title .word-blueprint { color: var(--blue); font-size: 86px; }
  .mind-illustration {
    position: absolute;
    left: 640px;
    top: 522px;
    width: 165px;
    height: 200px;
    border-radius: 48% 52% 42% 50%;
    background: linear-gradient(135deg, #e8302a 0%, #f7a21b 30%, #5cbf4a 55%, #3fa8e6 78%, #8a4fc9 100%);
    border: 5px solid var(--ink);
  }
  .edition-plate {
    position: absolute;
    left: 368px;
    top: 955px;
    width: 270px;
    height: 68px;
    background: var(--ink);
    border: 3px solid var(--yellow);
    display: flex;
    align-items: center;
    justify-content: center;
    color: var(--yellow);
    font-size: 30px;
    white-space: nowrap;
  }
  .subtitle {
    position: absolute;
    left: 104px;
    top: 1058px;
    width: 641px;
    text-align: center;
    color: var(--text-dark);
    font-size: 22px;
    line-height: 1.4;
  }
</style>
</head>
<body>
  <main class="cover">
    <div class="network-backdrop" role="img" aria-label="Light grey network of connected nodes and lines forming a large head silhouette"></div>
    <div class="spine-line"></div>
    <div class="author-plate">TOMAS VERADELLO</div>
    <div class="title-block"></div>
    <h1 class="title">
      <span class="word-brand">BRAND</span>
      <span class="word-voice">VOICE</span>
      <span class="word-blueprint">BLUEPRINT</span>
    </h1>
    <div class="mind-illustration" role="img" aria-label="Colourful mosaic illustration of a brain made of connected pieces"></div>
    <div class="edition-plate">3rd edition</div>
    <p class="subtitle">How to untangle the online attention puzzle<br>and leave your rivals behind</p>
  </main>
</body>
</html>
```